Commercial brochure presenting independent commercial activity

I would like to create a commercial brochure for my new professional activity.

This is a personal and not business oriented brochure because I will become an independent project assistant to assist engineering offices with one-off missions.

I want a 4 page A4 brochure

• Page 1: Logo, personal photo
• Page 2 and 3: Personal presentation and presentation of my activities
• Page4: contact information

My target audience: engineering offices and design offices

The objective of the brochure: it is to make my profile interesting so that design offices will want to use my services when there is demand

Sector of activity: food, chemical, pharmaceutical industry
The text of the brochure must remain in French and contain what is in the attached file

On page 1, you must keep a space for a photo of my profile which I will insert later because I do not have it yet and insert my monogram (it can be reworked to be inserted in the brochure)
The image with the logo (K/M) is the color range I want

engineering offices and design offices

industrie alimentaire, chimique, pharmaceutique

Sans Serif

0094D4
00A9DD
6FCCEA
C7EBF8
E9F6FB

• The plate must comply with current codes. Each reader must think that I am dynamic and that my services are of quality and equivalent to the presentation

```html
<!DOCTYPE html>
<html lang="fr">
<head>
<meta charset="UTF-8">
<title>Kévin Marchal – Assistant de projets indépendant</title>
<link rel="stylesheet" href="https://fonts.googleapis.com/css2?family=Montserrat:wght@300;400;500&family=Raleway:wght@300;400&display=swap">
<style>
  :root {
    --blue-deep: #0094D4;
    --blue: #00A9DD;
    --blue-sky: #6FCCEA;
    --blue-pale: #C7EBF8;
    --blue-mist: #E9F6FB;
    --white: #ffffff;
    --ink-soft: #5a6c78;
  }
  * { margin: 0; padding: 0; box-sizing: border-box; }
  html, body { width: 849px; height: 1200px; overflow: hidden; background: var(--white); }
  .brochure-cover {
    position: relative; width: 849px; height: 1200px; overflow: hidden;
    font-family: "Montserrat", Arial, sans-serif; background: var(--white);
  }
  .interior-photo {
    position: absolute; left: 0; top: 0; width: 502px; height: 305px;
    background: linear-gradient(135deg, #3b4a5c 0%, #6a7f94 45%, #2e3a48 100%);
  }
  .identity {
    position: absolute; left: 502px; top: 0; width: 347px; height: 305px;
    display: flex; flex-direction: column; align-items: center;
    padding-top: 62px;
  }
  .identity-mark {
    width: 92px; height: 92px; border-radius: 50%;
    border: 2px solid var(--blue-deep);
  }
  .identity-name {
    font-family: "Raleway", Arial, sans-serif; font-weight: 400;
    font-size: 27px; color: var(--blue-deep); letter-spacing: 0.5px;
    margin-top: 18px;
  }
  .identity-role {
    font-family: "Raleway", Arial, sans-serif; font-weight: 400;
    font-size: 11px; color: var(--ink-soft); margin-top: 6px;
  }
  .expertise-panel {
    position: absolute; left: 0; top: 305px; width: 502px; height: 612px;
    background: var(--blue);
  }
  .panel-dots {
    position: absolute; left: 62px; top: 38px; display: flex; gap: 10px;
  }
  .panel-dots span { width: 4px; height: 4px; border-radius: 50%; background: var(--white); }
  .expertise-label {
    position: absolute; left: 30px; top: 562px;
    transform: rotate(-90deg); transform-origin: left top;
    font-weight: 300; font-size: 37px; letter-spacing: 4px;
    color: var(--blue-mist); white-space: nowrap;
  }
  .expertise-list {
    position: absolute; left: 158px; top: 56px; width: 330px;
    list-style: none; display: flex; flex-direction: column; gap: 22px;
  }
  .expertise-title {
    font-weight: 300; font-size: 21px; line-height: 1.08;
    text-transform: uppercase; color: var(--blue-pale); letter-spacing: 0.4px;
    margin-bottom: 6px;
  }
  .expertise-items {
    list-style: none; font-weight: 400; font-size: 12.5px; line-height: 1.35; color: var(--white);
  }
  .portrait-photo {
    position: absolute; left: 502px; top: 305px; width: 347px; height: 612px;
    background: linear-gradient(180deg, #d9dde0 0%, #a9b0b5 55%, #6f777d 100%);
  }
  .experience-band {
    position: absolute; left: 0; top: 917px; width: 849px; height: 283px;
    background: var(--blue-mist);
  }
  .experience-title {
    position: absolute; left: 136px; top: 62px; width: 330px;
    font-weight: 400; font-size: 29px; line-height: 40px;
    letter-spacing: 3.5px; text-transform: uppercase; color: var(--blue-deep);
  }
  .experience-text {
    position: absolute; left: 504px; top: 22px; width: 330px;
    font-weight: 400; font-size: 20px; line-height: 34px; color: var(--blue-sky);
  }
</style>
</head>
<body>
<main class="brochure-cover">
  <div class="interior-photo" role="img" aria-label="Photo d'un bureau d'études moderne avec bibliothèque et grandes fenêtres"></div>

  <header class="identity">
    <div class="identity-mark"></div>
    <div class="identity-name">Kévin Marchal</div>
    <div class="identity-role">Assistant de projets indépendant</div>
  </header>

  <section class="expertise-panel">
    <div class="panel-dots"><span></span><span></span><span></span><span></span><span></span></div>
    <h2 class="expertise-label">MON EXPERTISE</h2>
    <ul class="expertise-list">
      <li>
        <h3 class="expertise-title">Conception<br>&amp; design</h3>
        <ul class="expertise-items">
          <li>Maquettes 3D (CadPlant 3D)</li>
          <li>Plans, schémas, P&amp;ID, Flowsheets</li>
          <li>Spécifications, catalogues, définition des fournitures</li>
        </ul>
      </li>
      <li>
        <h3 class="expertise-title">Rédaction<br>d'appels d'offre</h3>
        <ul class="expertise-items">
          <li>Préparation de budgets</li>
          <li>Réalisation de plannings</li>
          <li>Estimations budgétaires</li>
          <li>Réponse aux appels d'offre</li>
        </ul>
      </li>
      <li>
        <h3 class="expertise-title">Sécurité<br>machine</h3>
        <ul class="expertise-items">
          <li>Plans de montage</li>
          <li>Edition de PHS</li>
        </ul>
      </li>
      <li>
        <h3 class="expertise-title">Documentation<br>technique</h3>
        <ul class="expertise-items">
          <li>DESP</li>
          <li>Documentations spécifiques</li>
        </ul>
      </li>
    </ul>
  </section>

  <div class="portrait-photo" role="img" aria-label="Emplacement pour la photo de profil du consultant"></div>

  <section class="experience-band">
    <h2 class="experience-title">30 ans<br>d'expérience<br>dans l'industrie</h2>
    <p class="experience-text">Ma connaissance approfondie de la métallurgie (tuyauterie, serrurerie, chaudronnerie, charpente métallique, montage) me permet de garantir des études complètes et d'éviter les oublis.</p>
  </section>
</main>
</body>
</html>
```